Modern Business Card

Modern professional business card with more than just logo and demographic info. Something memorable.

We are a trendy/modern chiropractic group with an emphasis on neurology, hence the minimalist-type brain logo. We want to convey that modern and technical aspect with professionalism and the elite nature of our practice environment.

```html
<!DOCTYPE html>
<html lang="en">
<head>
<meta charset="utf-8">
<title>Kestrel Chiropractic – Business Card</title>
<link rel="stylesheet" href="https://fonts.googleapis.com/css2?family=Didact+Gothic&display=swap">
<style>
  :root {
    --brand-blue: #4a7fc1;
    --pattern-blue: #b9cbe9;
    --pattern-light: #dbe5f4;
    --ink: #1f2226;
    --paper: #ffffff;
    --backdrop: #eceff3;
  }
  * { margin: 0; padding: 0; box-sizing: border-box; }
  html, body {
    width: 1200px;
    height: 892px;
    overflow: hidden;
    background: var(--backdrop);
    font-family: "Didact Gothic", "Century Gothic", sans-serif;
  }
  .canvas { position: relative; width: 1200px; height: 892px; }
  .card {
    position: absolute;
    background: var(--paper);
    box-shadow: 0 6px 22px rgba(0, 0, 0, 0.14);
    overflow: hidden;
  }
  .card--front { left: 120px; top: 148px; width: 340px; height: 595px; }
  .card--back { left: 510px; top: 276px; width: 595px; height: 340px; }
  .card-art { display: block; width: 100%; height: 100%; }
  .ribbon { fill: var(--brand-blue); }
  .ribbon-gap { fill: var(--paper); }
  .brand-dot { fill: var(--brand-blue); }
  .brand-name { font-family: "Didact Gothic", "Century Gothic", sans-serif; fill: var(--ink); }
  .contact-number {
    font-family: "Didact Gothic", "Century Gothic", sans-serif;
    font-size: 17px;
    letter-spacing: 0.5px;
    fill: var(--paper);
  }
  .contact-icon { fill: none; stroke: var(--paper); stroke-width: 1.6; stroke-linecap: round; stroke-linejoin: round; }
  .office-hours { font-family: "Didact Gothic", "Century Gothic", sans-serif; font-size: 11px; fill: var(--brand-blue); }
  .back-pattern {
    position: absolute;
    inset: 0;
    background:
      linear-gradient(135deg, var(--pattern-light) 0%, var(--pattern-blue) 50%, var(--pattern-light) 100%);
  }
  .back-mark {
    position: absolute;
    left: 400px;
    top: 192px;
    display: flex;
    align-items: center;
    gap: 8px;
    padding: 6px 10px;
    background: var(--paper);
  }
  .back-mark-dot { width: 16px; height: 16px; border-radius: 50%; background: var(--brand-blue); }
  .back-mark-name { font-size: 15px; letter-spacing: 1.5px; color: var(--brand-blue); }
</style>
</head>
<body>
<main class="canvas">

  <section class="card card--front" aria-label="Business card front">
    <svg class="card-art" viewBox="0 0 340 595" xmlns="http://www.w3.org/2000/svg">
      <g class="brand-lockup">
        <circle class="brand-dot" cx="172" cy="106" r="14"/>
        <text class="brand-name" x="194" y="108" font-size="25" letter-spacing="1.5">KESTREL</text>
        <text class="brand-name" x="195" y="124" font-size="11.5" letter-spacing="1.2">CHIROPRACTIC</text>
      </g>

      <g class="ribbon-top">
        <rect class="ribbon" x="-40" y="-40" width="110" height="302"/>
        <rect class="ribbon" x="-40" y="200" width="280" height="62" rx="31"/>
        <rect class="ribbon-gap" x="70" y="-40" width="400" height="240" rx="31"/>
      </g>

      <g class="contact-line contact-line--phone">
        <rect class="ribbon" x="-40" y="282" width="350" height="62" rx="31"/>
        <text class="contact-number" x="262" y="319" text-anchor="end">5550142870</text>
        <path class="contact-icon" d="M279 305 q-2 2 0 6 l5 6 q4 3 6 1 l1.5-2 -3.5-3 -2 1.5 -3-4 1.5-2 -3-3.5 z"/>
      </g>

      <g class="contact-line contact-line--fax">
        <rect class="ribbon" x="-40" y="364" width="370" height="166" rx="31"/>
        <rect class="ribbon-gap" x="170" y="430" width="250" height="40" rx="20"/>
        <text class="contact-number" x="278" y="401" text-anchor="end">5550142871</text>
        <rect class="contact-icon" x="290" y="390" width="14" height="9" rx="1.5"/>
        <rect class="contact-icon" x="293" y="385" width="8" height="5"/>
        <rect class="contact-icon" x="293" y="396" width="8" height="6"/>
      </g>

      <rect class="ribbon" x="-40" y="555" width="200" height="100" rx="40"/>

      <text class="office-hours" x="330" y="585" text-anchor="end">Monday-Friday 9-6&#160;&#160;&#160;Saturday 10-6</text>
    </svg>
  </section>

  <section class="card card--back" aria-label="Business card back">
    <div class="back-pattern" role="img" aria-label="Repeating pattern of the practice's brain symbol in light blue on white"></div>
    <div class="back-mark">
      <span class="back-mark-dot"></span>
      <span class="back-mark-name">KESTREL</span>
    </div>
  </section>

</main>
</body>
</html>
```